Real estate website

Please find attached a rough outline of what we want for the design. This is just for placement to show what to have on the menu's as content, etc. but please make it look much more professional.
Please make the bottom footer a similar gradient to the logo
Please make the sign up now and log in buttons look better - these are just samples to show placement
Please use the correct logos for brindlequay.com.au, tovrel.com.au and quintaro.com.au
Where it has 'video embed' just leave that as is as we will replace that with a video.

```html
<!DOCTYPE html>
<html lang="en">
<head>
<meta charset="utf-8">
<title>Listwell – Get Your Free Guide</title>
<link href="https://fonts.googleapis.com/css2?family=Archivo:wght@700;800&family=Roboto:wght@300;400;500;700&display=swap" rel="stylesheet">
<style>
:root{
  --green-dark:#1d7a32;
  --green-mid:#2f8a34;
  --green-lime:#8cc828;
  --green-accent:#7dbb2a;
  --text-dark:#111;
  --text-body:#666;
  --field-bg:#fff;
  --line:#e2e2e2;
}
*{box-sizing:border-box;margin:0;padding:0}
html,body{width:1200px;height:947px;overflow:hidden;background:#fff;font-family:'Roboto',sans-serif;color:var(--text-dark)}
.site-header{position:absolute;left:0;top:0;width:1200px;height:97px;border-bottom:1px solid var(--line)}
.brand{position:absolute;left:111px;top:28px;font-size:34px;font-weight:300;color:#333;letter-spacing:.3px}
.main-nav{position:absolute;left:363px;top:42px;display:flex;gap:24px}
.main-nav a{font-size:11.5px;font-weight:700;color:#111;text-decoration:none;letter-spacing:.1px}
.btn-signup{position:absolute;left:804px;top:23px;width:137px;height:52px;background:linear-gradient(90deg,var(--green-dark),var(--green-lime));color:#fff;font-weight:700;font-size:15.5px;display:flex;align-items:center;justify-content:center}
.btn-login{position:absolute;left:951px;top:23px;width:137px;height:52px;border:2px solid;border-image:linear-gradient(90deg,var(--green-dark),var(--green-lime)) 1;color:#111;font-weight:700;font-size:15.5px;display:flex;align-items:center;justify-content:center;gap:9px}
.video-frame{position:absolute;left:111px;top:137px;width:489px;height:386px;background:#fff;box-shadow:0 0 8px rgba(0,0,0,.12);padding:6px}
.video-still{position:relative;width:100%;height:100%;background:linear-gradient(135deg,#8ade5a 0%,#58c65a 50%,#2eb062 100%)}
.play{position:absolute;left:50%;top:50%;transform:translate(-50%,-50%)}
.guide{position:absolute;left:659px;top:145px;width:429px}
.guide h1{font-family:'Archivo',sans-serif;font-weight:800;font-size:20.5px;letter-spacing:.4px;color:var(--text-dark)}
.guide p{margin-top:13px;font-size:13.5px;color:#555}
.field{position:absolute;left:660px;width:428px;height:46px;background:var(--field-bg);box-shadow:0 2px 5px rgba(0,0,0,.1);display:flex;align-items:center;padding-left:16px;gap:11px;font-size:14.5px;color:#444}
.submit{position:absolute;left:660px;top:464px;width:428px;height:47px;background:linear-gradient(90deg,var(--green-mid) 35%,var(--green-lime) 75%);color:#fff;font-weight:700;font-size:15px;display:flex;align-items:center;justify-content:center}
.offer{position:absolute;left:0;top:573px;width:1200px;text-align:center;font-family:'Archivo',sans-serif;font-weight:800;font-size:22.5px;letter-spacing:.5px}
.offer span{color:var(--green-accent)}
.intro{position:absolute;left:120px;top:624px;width:960px;text-align:center;font-size:14.5px;line-height:25.8px;color:var(--text-body);font-weight:300}
.listing{position:absolute;top:731px;display:flex;align-items:center;gap:22px;font-size:18px;font-weight:500;color:#333}
.site-footer{position:absolute;left:0;top:810px;width:1200px;height:137px;background:linear-gradient(90deg,#0d6b3a 0%,#16763a 45%,#6ea82c 80%,#86be2a 100%);color:#fff}
.footer-nav{position:absolute;left:0;top:39px;width:1200px;display:flex;justify-content:center;gap:18px;font-size:14px;font-weight:700}
.footer-nav .sep{font-weight:400}
.footer-rule{position:absolute;left:111px;top:79px;width:977px;height:1px;background:rgba(255,255,255,.85)}
.copyright{position:absolute;left:0;top:98px;width:1200px;text-align:center;font-size:14px}
.code{position:absolute;left:1130px;top:103px;font-size:12px}
</style>
</head>
<body>
<header class="site-header">
  <div class="brand">Listwell</div>
  <nav class="main-nav"><a href="#">SELL MY PROPERTY</a><a href="#">RENT MY PROPERTY</a><a href="#">RENTAL MANAGEMENT</a></nav>
  <a class="btn-signup">SIGN UP NOW</a>
  <a class="btn-login">
    <svg width="16" height="16" viewBox="0 0 16 16"><circle cx="8" cy="8" r="7" fill="none" stroke="#111" stroke-width="1.6"/><circle cx="8" cy="6.3" r="2.4" fill="#111"/><path d="M3.6 12.5c1-2 2.6-2.8 4.4-2.8s3.4.8 4.4 2.8" fill="#111"/></svg>
    LOGIN</a>
</header>

<div class="video-frame">
  <div class="video-still" role="img" aria-label="Video embed: presenter introducing the free guide">
    <svg class="play" width="90" height="90" viewBox="0 0 90 90"><circle cx="45" cy="45" r="42" fill="rgba(255,255,255,.35)"/><circle cx="45" cy="45" r="29" fill="#fff"/><path d="M39 35l16 10-16 10z" fill="#2f8a34"/></svg>
  </div>
</div>

<section class="guide">
  <h1>LISTWELL GET YOUR FREE GUIDE</h1>
  <p>Get Your Free Guide To listing privately in the ACT</p>
</section>
<div class="field" style="top:228px"><svg width="12" height="14" viewBox="0 0 12 14"><circle cx="6" cy="4" r="3.2" fill="#a8d580"/><path d="M0 14c0-4 2.7-6 6-6s6 2 6 6z" fill="#a8d580"/></svg>First Name</div>
<div class="field" style="top:287px"><svg width="12" height="14" viewBox="0 0 12 14"><circle cx="6" cy="4" r="3.2" fill="#a8d580"/><path d="M0 14c0-4 2.7-6 6-6s6 2 6 6z" fill="#a8d580"/></svg>Last Name</div>
<div class="field" style="top:346px"><svg width="13" height="13" viewBox="0 0 13 13"><path d="M2.5 0.5l2.3 2.8-1.3 1.6c.9 1.9 2.3 3.3 4.2 4.2l1.6-1.3 2.8 2.3-1.2 2.2C5.6 11.8 1.2 7.4 0.7 1.7z" fill="#a8d580"/></svg>Phone</div>
<div class="field" style="top:405px"><svg width="15" height="11" viewBox="0 0 15 11"><rect width="15" height="11" fill="#a8d580"/><path d="M0 0l7.5 6L15 0" fill="none" stroke="#fff" stroke-width="1.3"/></svg>Email</div>
<a class="submit">SUBMIT</a>

<h2 class="offer">WANT TO PAY NOTHING UPFRONT? ASK US HOW – <span>044 510 2863</span></h2>
<p class="intro">Listing a house in Australia for sale or rental is costly! In the ACT, it's even worse! ACT residents are paying more to list and sell online, than in other parts of Australia. Listwell solves this problem for you. Sell or rent your own home privately in the ACT with Listwell and pay zero commission. You'll be listed for an unlimited time on all the major sites. All the tools for listing are inside your account, sign up today and get started.</p>

<div class="listing" style="left:255px"><svg width="28" height="26" viewBox="0 0 28 26"><rect x="1.5" y="3.5" width="21" height="21" rx="2" fill="none" stroke="#222" stroke-width="2.4"/><path d="M6 13l5 5L26 2" fill="none" stroke="#4caa2e" stroke-width="3.4"/></svg>brindlequay.com.au</div>
<div class="listing" style="left:572px"><svg width="28" height="26" viewBox="0 0 28 26"><rect x="1.5" y="3.5" width="21" height="21" rx="2" fill="none" stroke="#222" stroke-width="2.4"/><path d="M6 13l5 5L26 2" fill="none" stroke="#4caa2e" stroke-width="3.4"/></svg>tovrel.com.au</div>
<div class="listing" style="left:800px"><svg width="28" height="26" viewBox="0 0 28 26"><rect x="1.5" y="3.5" width="21" height="21" rx="2" fill="none" stroke="#222" stroke-width="2.4"/><path d="M6 13l5 5L26 2" fill="none" stroke="#4caa2e" stroke-width="3.4"/></svg>quintaro.com.au</div>

<footer class="site-footer">
  <nav class="footer-nav"><span>FINANCE</span><span class="sep">|</span><span>CONVEYANCING</span><span class="sep">|</span><span>BUILDING INSPECTION</span><span class="sep">|</span><span>PEST INSPECTION</span><span class="sep">|</span><span>VALUATION</span><span class="sep">|</span><span>MARKET APPRAISAL</span></nav>
  <div class="footer-rule"></div>
  <div class="copyright">© 2022 Listwell &nbsp;|&nbsp; All Rights Reserved</div>
  <div class="code">C45</div>
</footer>
</body>
</html>
```